BRIGHTDESK COWORKING Website design and coding

BRIGHTDESK COWORKING

BRIGHTDESK is Galveston’s first (and currently only) shared business co-working space. We share the same upscale, casual work environment, but we work independently on our own (or our team’s) projects and goals. For only a flat $195 membership fee per month, you have your very own all-inclusive, fun, personal business office environment. Website is written (Word file #12, below); and all pictures etc provided. Galveston is a beachy, coastal, historic city an hour from Houston, Texas USA. Logo (file 11 below) is temporary only.

Target Market(s)

Outside sales people, medical students looking for study hall, Houston companies looking for local office, real estate agents, graphic artists, entrepreneurs, etc

Contact Information for Business Card

will discuss --want to combine with current business card with multiple businesses

Logo Text

BRIGHTDESK COWORKING

Coding

Coded - Design and coding required

Number of Pages Required

5+ page

Colors
ec1f27
fbed22

Requirements
Nice to have
• maroon/wine dominant with yellow and red accents, gray base are the colors of the space--website could coordinate--but open to creative ideas/combinations

```html
<!DOCTYPE html>
<html lang="en">
<head>
<meta charset="utf-8">
<title>BRIGHTDESK COWORKING</title>
<link href="https://fonts.googleapis.com/css2?family=Exo+2:wght@400;500;700;800&family=Roboto:wght@400;500;700&display=swap" rel="stylesheet">
<style>
:root{
  --red:#d71920;
  --red-dark:#a30f16;
  --wine:#7a0d12;
  --ink:#151515;
  --text:#555;
  --gray-bg:#ececec;
  --footer:#1f1f1f;
  --footer-text:#8a8a8a;
  --white:#fff;
}
*{margin:0;padding:0;box-sizing:border-box}
html,body{width:1200px;height:4335px;overflow:hidden}
body{position:relative;background:var(--white);font-family:"Roboto",Arial,sans-serif;color:var(--ink)}
.abs{position:absolute}
.heading{font-family:"Exo 2",Arial,sans-serif;font-weight:800;letter-spacing:.5px;white-space:nowrap}
.btn{position:absolute;display:flex;align-items:center;justify-content:center;gap:8px;border-radius:30px;background:var(--red-dark);color:#fff;font:700 14px "Roboto",Arial,sans-serif;text-transform:uppercase}
.btn .arr{width:14px;height:14px;border-radius:50%;background:#fff;position:relative}
.btn .arr::after{content:"";position:absolute;left:5px;top:4px;border-left:6px solid var(--red-dark);border-top:3px solid transparent;border-bottom:3px solid transparent}
.deco{position:absolute;width:138px;height:12px;left:50%;margin-left:-69px}
.hex{clip-path:polygon(50% 0,100% 25%,100% 75%,50% 100%,0 75%,0 25%)}

/* header */
.brand{left:96px;top:30px;width:220px;text-align:center;font:400 30px/38px "Exo 2",Arial,sans-serif;color:#fff;letter-spacing:1px;z-index:3}
.nav a{color:#fff;font:500 14.5px "Roboto",Arial,sans-serif;text-decoration:none;position:absolute;white-space:nowrap}
.nav a.active{color:var(--red)}
.nav a.active::after{content:"";position:absolute;left:0;right:0;bottom:-6px;height:2px;background:var(--red)}
.call{left:776px;top:28px;z-index:3;color:#fff}
.call small{display:block;font:400 11px "Roboto",sans-serif;padding-left:32px}
.call strong{display:block;font:700 18px "Exo 2",sans-serif;padding-left:32px;letter-spacing:.5px}
.call svg{position:absolute;left:0;top:4px}
.signup{left:971px;top:29px;width:116px;height:35px;background:var(--red);font-size:14px;text-transform:none}

/* hero */
.hero{left:0;top:0;width:1200px;height:790px}
.hero-title{left:0;width:1200px;top:286px;text-align:center;font-size:46px;color:#fff;z-index:2}
.hero-sub{left:330px;width:540px;top:365px;text-align:center;color:#fff;font:400 15.5px/27px "Roboto",sans-serif;z-index:2}
.hero-band{left:353px;top:272px;width:488px;height:145px;background:rgba(40,35,30,.45)}
.hero-cta{left:498px;top:443px;width:204px;height:45px;background:var(--red);font-size:15px}
.slider-arrow{width:34px;height:34px;border:2px solid #fff;border-radius:50%;z-index:2}

/* about */
.label{font:700 18px "Exo 2",sans-serif;color:var(--red)}
.about-title{left:111px;top:873px;font-size:34px}
.about-text{left:111px;top:941px;width:440px;font:400 13.5px/27.5px "Roboto",sans-serif;color:var(--text)}

/* amenities */
.amenities{left:0;top:1284px;width:1200px;height:808px;background:linear-gradient(180deg,#efefef,#e6e6e6)}
.sec-title{left:0;width:1200px;text-align:center;font-size:34px}
.amen-intro{left:250px;width:700px;top:1401px;text-align:center;font:400 14px/26px "Roboto",sans-serif;color:var(--text)}
.amen-item{position:absolute;width:260px;text-align:center;font:500 14.5px/24px "Roboto",sans-serif;color:var(--ink)}
.amen-hex{position:absolute;width:111px;height:126px;filter:drop-shadow(0 3px 6px rgba(0,0,0,.15))}
.amen-hex .hex{width:100%;height:100%;background:#fff;display:flex;align-items:center;justify-content:center}

/* membership */
.membership{left:0;top:2092px;width:1200px;height:312px;background:linear-gradient(90deg,#c8141b,#d71920 50%,#c8141b)}
.mem-title{top:2125px;color:#fff;font-size:40px}
.mem-text{left:160px;width:880px;text-align:center;color:#fff;font:400 14.5px/25px "Roboto",sans-serif}
.mem-btn{left:515px;top:2319px;width:168px;height:42px;background:var(--ink);text-transform:uppercase}

/* pictures */
.pic{position:absolute;width:315px;height:222px}

/* philosophy */
.phil-title{left:634px;top:3298px;font-size:32px}
.phil-sub{left:719px;top:3405px;font:700 18px "Roboto",sans-serif}
.phil-text{left:634px;top:3462px;width:442px;font:400 13.5px/26px "Roboto",sans-serif;color:var(--text)}

/* footer */
.footer{left:0;top:3834px;width:1200px;height:441px;background:var(--footer)}
.f-head{font:700 14px "Roboto",sans-serif;color:#fff}
.f-text{font:400 11.5px/18px "Roboto",sans-serif;color:var(--footer-text)}
.f-link{position:absolute;font:400 11.5px "Roboto",sans-serif;color:var(--footer-text)}
.f-brand{left:80px;top:4088px;width:240px;text-align:center;font:400 30px/38px "Exo 2",sans-serif;color:#cfcfcf;letter-spacing:1px}
.f-input{left:703px;top:4133px;width:265px;height:44px;border-radius:24px;background:#fff;font:400 12px/44px "Roboto",sans-serif;color:#555;padding-left:20px}
.f-sub{left:974px;top:4133px;width:113px;height:44px;background:var(--red);font-size:14px}
.social{width:30px;height:30px;border-radius:50%;border:1px solid #555;background:#2c2c2c}
.bottom-bar{left:0;top:4275px;width:1200px;height:60px;background:var(--red)}
.bottom-bar span{position:absolute;top:23px;color:#fff;font:400 12px "Roboto",sans-serif}
</style>
</head>
<body>

<!-- HERO -->
<svg class="abs hero" viewBox="0 0 1200 790" role="img" aria-label="Photo of the coworking lounge with sofas, pendant lamps and desks">
  <defs>
    <linearGradient id="heroFill" x1="0" y1="0" x2="0.4" y2="1">
      <stop offset="0" stop-color="#2e2a22"/>
      <stop offset="0.45" stop-color="#5a5232"/>
      <stop offset="0.75" stop-color="#7d7436"/>
      <stop offset="1" stop-color="#3b3626"/>
    </linearGradient>
  </defs>
  <path d="M0 0H1200V470C1160 500 1140 560 1105 610C1040 690 920 660 760 680C600 700 470 720 380 760C320 786 260 790 210 775C110 745 40 690 0 640Z" fill="url(#heroFill)"/>
</svg>
<div class="abs hero-band"></div>
<div class="abs heading hero-title">BRIGHTDESK COWORK</div>
<div class="abs hero-sub">BRIGHTDESK is Galveston's first (and currently only) shared business co-working space.</div>
<div class="btn hero-cta">Get Started <span class="arr"></span></div>
<div class="abs slider-arrow" style="left:35px;top:355px"></div>
<svg class="abs" style="left:35px;top:355px;z-index:3" width="34" height="34"><path d="M19 11l-6 6 6 6" stroke="#fff" stroke-width="2" fill="none"/></svg>
<div class="abs slider-arrow" style="left:1127px;top:355px"></div>
<svg class="abs" style="left:1127px;top:355px;z-index:3" width="34" height="34"><path d="M15 11l6 6-6 6" stroke="#fff" stroke-width="2" fill="none"/></svg>

<div class="abs brand">BRIGHTDESK<br>COWORKING</div>
<nav class="abs nav" style="left:0;top:87px;width:1200px;height:20px;z-index:3">
  <a class="active" style="left:415px">Home</a>
  <a style="left:478px">About</a>
  <a style="left:542px">Amenities</a>
  <a style="left:634px">Membership</a>
  <a style="left:743px">Pictures</a>
  <a style="left:822px">The Brightdesk Philosophy</a>
  <a style="left:1033px">Contact</a>
</nav>
<div class="abs call">
  <svg width="22" height="30" viewBox="0 0 22 30"><rect x="1" y="1" width="20" height="28" rx="3" fill="none" stroke="var(--red)" stroke-width="2"/><path d="M7 9c0 6 3 10 8 12l2-3-3-2-2 1c-2-1-3-3-3-5l1-2-2-3z" fill="var(--red)"/></svg>
  <small>Call Us</small>
  <strong>713-555-0142</strong>
</div>
<div class="btn signup">
  <svg width="14" height="15" viewBox="0 0 14 15"><rect x="2" y="6" width="10" height="8" rx="1" fill="none" stroke="#fff" stroke-width="1.6"/><path d="M4 6V4a3 3 0 0 1 6 0v2" fill="none" stroke="#fff" stroke-width="1.6"/></svg>
  Sign Up
</div>

<!-- ABOUT -->
<div class="abs label" style="left:111px;top:843px">ABOUT</div>
<div class="abs heading about-title">BRIGHTDESK COWORKING</div>
<p class="abs about-text">BRIGHTDESK is Galveston's first (and currently only) shared business co-working space. We share the same upscale, casual work environment, but we work independently on our own (or our team's) projects and goals. For only a flat $195 membership fee per month, you have your very own all-inclusive, fun, personal business office environment.</p>
<div class="btn" style="left:111px;top:1139px;width:158px;height:42px">Learn More <span class="arr"></span></div>

<div class="abs hex" style="left:770px;top:815px;width:346px;height:395px;background:var(--red)"></div>
<div class="abs hex" role="img" aria-label="Photo of the kitchen with a wooden bar counter and pendant lamps" style="left:754px;top:808px;width:346px;height:395px;background:linear-gradient(160deg,#caa86a,#8d6a38 55%,#3c2e22)"></div>
<div class="abs hex" role="img" aria-label="Photo of the office corridor" style="left:1028px;top:739px;width:118px;height:130px;background:linear-gradient(160deg,#8c8c86,#5a5a55)"></div>
<div class="abs hex" role="img" aria-label="Photo of a private cubicle with a desk chair" style="left:608px;top:986px;width:118px;height:131px;background:linear-gradient(160deg,#9a9a92,#3d3c35)"></div>

<!-- AMENITIES -->
<div class="abs amenities" role="img" aria-label="Faded photo of the open office space"></div>
<div class="abs heading sec-title" style="top:1330px">AMENITIES</div>
<svg class="deco" style="top:1377px" viewBox="0 0 138 12"><line x1="0" y1="6" x2="40" y2="6" stroke="var(--red)" stroke-width="3"/><line x1="98" y1="6" x2="138" y2="6" stroke="var(--red)" stroke-width="3"/><circle cx="53" cy="6" r="3.5" fill="var(--red)"/><circle cx="69" cy="6" r="6" fill="var(--ink)"/><circle cx="85" cy="6" r="3.5" fill="var(--red)"/></svg>
<p class="abs amen-intro">BRIGHTDESK is the first Galveston co-working space, and offers all of the following features, all included in your monthly $195 membership fee:</p>

<!-- row 1 -->
<div class="amen-hex" style="left:161px;top:1475px"><div class="hex">
  <svg width="60" height="60" viewBox="0 0 60 60" fill="none" stroke="var(--ink)" stroke-width="2"><rect x="12" y="18" width="22" height="36"/><rect x="34" y="30" width="14" height="24"/><rect x="26" y="8" width="10" height="10" stroke="var(--red)"/><path d="M17 24h4M25 24h4M17 32h4M25 32h4M17 40h4M25 40h4M38 36h6M38 44h6" stroke="var(--red)"/><path d="M20 54v-8h6v8"/></svg>
</div></div>
<div class="amen-item" style="left:87px;top:1619px">Open office or a private cubicle<br>for your daily use.</div>

<div class="amen-hex" style="left:414px;top:1475px"><div class="hex">
  <svg width="60" height="60" viewBox="0 0 60 60" fill="none" stroke-width="2.5"><path d="M10 24a28 28 0 0 1 40 0M16 30a20 20 0 0 1 28 0M22 36a12 12 0 0 1 16 0" stroke="var(--ink)"/><rect x="12" y="40" width="36" height="14" rx="7" stroke="var(--red)"/><path d="M20 44v6M24 44v6M30 44v6M36 44v6" stroke="var(--red)" stroke-width="1.5"/></svg>
</div></div>
<div class="amen-item" style="left:340px;top:1619px">Free Wifi</div>

<div class="amen-hex" style="left:667px;top:1475px"><div class="hex">
  <svg width="60" height="60" viewBox="0 0 60 60" fill="none" stroke-width="2"><circle cx="32" cy="26" r="14" stroke="var(--red)"/><path d="M28 26h8M32 22v4" stroke="var(--red)"/><path d="M8 38l12 12 10-4 12-4-4-6-10 2" stroke="var(--ink)"/><path d="M8 38l6-6 8 4" stroke="var(--ink)"/></svg>
</div></div>
<div class="amen-item" style="left:593px;top:1619px">24 hour access</div>

<div class="amen-hex" style="left:904px;top:1475px"><div class="hex" role="img" aria-label="Illustration of a casual open workspace" style="background:linear-gradient(160deg,#e2323a,#a9121a)"></div></div>
<div class="amen-item" style="left:830px;top:1619px;width:260px">Comfortable open casual spaces<br>or private office cubicles</div>

<!-- row 2 -->
<div class="amen-hex" style="left:161px;top:1691px"><div class="hex">
  <svg width="60" height="60" viewBox="0 0 60 60" fill="none" stroke-width="2"><path d="M12 28h30v10a12 12 0 0 1-12 12h-6a12 12 0 0 1-12-12z" stroke="var(--ink)"/><path d="M42 32h4a5 5 0 0 1 0 10h-6" stroke="var(--ink)"/><path d="M8 54h40" stroke="var(--ink)"/><path d="M20 12c-3 4 3 6 0 10M27 12c-3 4 3 6 0 10M34 12c-3 4 3 6 0 10" stroke="var(--red)"/></svg>
</div></div>
<div class="amen-item" style="left:87px;top:1834px">Communal coffee bar and kitchen,<br>with FREE coffee.</div>

<div class="amen-hex" style="left:414px;top:1691px"><div class="hex">
  <svg width="60" height="60" viewBox="0 0 60 60" fill="none" stroke-width="2"><rect x="38" y="22" width="12" height="30" rx="2" stroke="var(--ink)"/><path d="M42 22v-6h6M44 16v-4" stroke="var(--ink)"/><path d="M8 40c6-4 12-4 18 0l8 2v6H14" stroke="var(--ink)"/><circle cx="20" cy="28" r="2" stroke="var(--red)"/><circle cx="28" cy="22" r="2" stroke="var(--red)"/><circle cx="30" cy="32" r="1.5" stroke="var(--red)"/></svg>
</div></div>
<div class="amen-item" style="left:340px;top:1834px">Health and social distance<br>amenities, including hand<br>washing stations,</div>

<div class="amen-hex" style="left:667px;top:1691px"><div class="hex">
  <svg width="60" height="60" viewBox="0 0 60 60" fill="none" stroke-width="2"><rect x="18" y="10" width="24" height="12" stroke="var(--ink)"/><rect x="8" y="22" width="44" height="20" rx="2" stroke="var(--ink)"/><rect x="16" y="36" width="28" height="16" stroke="var(--ink)"/><path d="M20 42h20M20 47h14" stroke="var(--red)"/><circle cx="44" cy="28" r="1.5" fill="var(--red)" stroke="none"/></svg>
</div></div>
<div class="amen-item" style="left:593px;top:1834px">Use of copier/printer</div>

<div class="amen-hex" style="left:904px;top:1691px"><div class="hex">
  <svg width="60" height="60" viewBox="0 0 60 60" fill="none" stroke-width="2"><rect x="20" y="8" width="20" height="44" rx="4" stroke="var(--ink)"/><path d="M25 18h3M32 18h3M25 25h3M32 25h3M25 32h3M32 32h3" stroke="var(--ink)"/><rect x="26" y="38" width="8" height="8" stroke="var(--red)"/><path d="M14 20a14 14 0 0 0 0 20M46 20a14 14 0 0 1 0 20M9 16a20 20 0 0 0 0 28M51 16a20 20 0 0 1 0 28" stroke="var(--red)"/></svg>
</div></div>
<div class="amen-item" style="left:830px;top:1834px">Keyless, digital door entry</div>

<div class="btn" style="left:518px;top:1966px;width:164px;height:42px">Learn More <span class="arr"></span></div>

<!-- MEMBERSHIP -->
<div class="abs membership" role="img" aria-label="Red-tinted photo of the office interior"></div>
<div class="abs heading sec-title mem-title">MEMBERSHIP</div>
<p class="abs mem-text" style="top:2191px">For only $195 a month, charged to your credit card, you get the all-inclusive amenities listed above, for one flat fee. The only "extras" are for copies, on a per-copy basis.</p>
<p class="abs mem-text" style="top:2248px">WiFi, coffee, use of the conference room, office use, use of the kitchen and all the other features listed under "AMENITIES" above, are INCLUDED at no additional cost.</p>
<div class="btn mem-btn">Get A Free Day</div>

<!-- PICTURES -->
<div class="abs heading sec-title" style="top:2496px">PICTURES</div>
<svg class="deco" style="top:2545px" viewBox="0 0 138 12"><line x1="0" y1="6" x2="40" y2="6" stroke="var(--red)" stroke-width="3"/><line x1="98" y1="6" x2="138" y2="6" stroke="var(--red)" stroke-width="3"/><circle cx="53" cy="6" r="3.5" fill="var(--red)"/><circle cx="69" cy="6" r="6" fill="var(--ink)"/><circle cx="85" cy="6" r="3.5" fill="var(--red)"/></svg>

<div class="pic" role="img" aria-label="Photo of the copier area and hallway" style="left:111px;top:2597px;background:linear-gradient(135deg,#c9b08a,#8e8e88 55%,#5d5b55)"></div>
<div class="pic" role="img" aria-label="Photo of wooden desks under pendant lamps" style="left:443px;top:2597px;background:linear-gradient(180deg,#5a5448,#c8a15c 55%,#9a7a40)"></div>
<div class="pic" role="img" aria-label="Photo of the glass-walled kitchen" style="left:774px;top:2597px;background:linear-gradient(135deg,#a09c90,#d8c79e 50%,#6d6658)"></div>
<div class="pic" role="img" aria-label="Photo of the lounge with plants and blinds" style="left:111px;top:2838px;background:linear-gradient(135deg,#2e2e2c,#6a6660 50%,#b9a97a)"></div>
<div class="pic" role="img" aria-label="Photo of a cubicle with a yellow chair" style="left:443px;top:2838px;background:linear-gradient(135deg,#b8b6ad,#8c8a80 55%,#3e3d38)"></div>
<div class="pic" role="img" aria-label="Photo of red lockers and a leather sofa" style="left:774px;top:2838px;background:linear-gradient(135deg,#7c1a20,#c8c6c0 55%,#2c2a28)"></div>

<div class="btn" style="left:490px;top:3117px;width:219px;height:45px;background:var(--red);font-size:15px">See All Pictures <span class="arr"></span></div>

<!-- PHILOSOPHY -->
<div class="abs hex" style="left:82px;top:3295px;width:361px;height:402px;background:var(--red-dark)"></div>
<div class="abs hex" role="img" aria-label="Photo of the kitchen counter with bar stools" style="left:100px;top:3310px;width:343px;height:382px;background:linear-gradient(170deg,#d9d1b8,#8a4a3a 55%,#2d1b1a)"></div>
<div class="abs hex" role="img" aria-label="Photo of a plant beside the lounge" style="left:50px;top:3226px;width:118px;height:132px;background:linear-gradient(160deg,#4f4a3c,#a58e5c)"></div>
<div class="abs hex" role="img" aria-label="Photo of the open workspace from above" style="left:470px;top:3473px;width:118px;height:134px;background:linear-gradient(160deg,#3a4656,#c8a04a)"></div>

<div class="abs heading phil-title">THE BRIGHTDESK PHILOSOPHY</div>
<svg class="abs" style="left:634px;top:3346px" width="138" height="12" viewBox="0 0 138 12"><line x1="0" y1="6" x2="40" y2="6" stroke="var(--red)" stroke-width="3"/><line x1="98" y1="6" x2="138" y2="6" stroke="var(--red)" stroke-width="3"/><circle cx="53" cy="6" r="3.5" fill="var(--red)"/><circle cx="69" cy="6" r="6" fill="var(--ink)"/><circle cx="85" cy="6" r="3.5" fill="var(--red)"/></svg>
<div class="abs" style="left:634px;top:3378px;width:71px;height:71px;border-radius:50%;background:var(--wine)"></div>
<div class="abs phil-sub">WORK OUTSIDE THE HOME</div>
<p class="abs phil-text">Free yourself for the burdens of house or school, and work in an environment that MOTIVATES you instead of DISTRACTS you. Meet like-minded people that can help you along, and yet you have the option to work in a quiet-and very comfortable – private office cubicle. Perfect for medical students, entrepreneurs, designers, writers, business reps away from headquarters,</p>
<div class="btn" style="left:634px;top:3649px;width:159px;height:40px;background:var(--red)">Learn More <span class="arr"></span></div>

<!-- FOOTER -->
<div class="abs footer"></div>

<svg class="abs" style="left:112px;top:3878px" width="38" height="42" viewBox="0 0 38 42" fill="none" stroke="var(--red)" stroke-width="2.5"><path d="M19 4a11 11 0 0 1 11 11c0 8-11 19-11 19S8 23 8 15A11 11 0 0 1 19 4z"/><circle cx="19" cy="15" r="4"/><path d="M6 38h26"/></svg>
<div class="abs f-head" style="left:167px;top:3876px">Address</div>
<div class="abs f-text" style="left:167px;top:3897px">Brightdesk Coworking<br>410 Harbor Ave, Suite 101<br>Galveston, TX 77550</div>

<svg class="abs" style="left:318px;top:3878px" width="38" height="42" viewBox="0 0 38 42" fill="none" stroke="var(--red)" stroke-width="2.5"><path d="M19 4a11 11 0 0 1 11 11c0 8-11 19-11 19S8 23 8 15A11 11 0 0 1 19 4z"/><circle cx="19" cy="15" r="4"/><path d="M6 38h26"/></svg>
<div class="abs f-head" style="left:372px;top:3876px">Mailing address</div>
<div class="abs f-text" style="left:372px;top:3897px">Marlow Holdings<br>85 Elm St, Suite 200<br>Houston, TX 77002</div>

<svg class="abs" style="left:526px;top:3885px" width="38" height="36" viewBox="0 0 38 36" fill="none" stroke="var(--red)" stroke-width="2.5"><path d="M4 12c0-5 6-8 15-8s15 3 15 8l-6 3-3-4H13l-3 4z"/><path d="M9 18l-3 14h26l-3-14z"/><circle cx="19" cy="24" r="4"/></svg>
<div class="abs f-head" style="left:572px;top:3884px">Contact Info</div>
<div class="abs f-text" style="left:572px;top:3906px">713-555-0142</div>

<svg class="abs" style="left:705px;top:3886px" width="38" height="32" viewBox="0 0 38 32" fill="none" stroke="var(--red)" stroke-width="2.5"><rect x="3" y="4" width="32" height="24" rx="2"/><path d="M3 6l16 12L35 6"/></svg>
<div class="abs f-head" style="left:752px;top:3884px">Email Address</div>
<div class="abs f-text" style="left:752px;top:3906px">hello@brightdeskmail.com</div>

<div class="btn" style="left:937px;top:3889px;width:150px;height:42px;background:var(--red);font-size:13px">Get In Touch</div>

<div class="abs" style="left:111px;top:3984px;width:978px;height:1px;background:#3a3a3a"></div>

<div class="abs f-brand">BRIGHTDESK<br>COWORKING</div>

<div class="abs f-head" style="left:365px;top:4037px;font-size:12.5px">COMPANY</div>
<span class="f-link" style="left:365px;top:4075px">Home</span>
<span class="f-link" style="left:365px;top:4102px">About</span>
<span class="f-link" style="left:365px;top:4129px">Amenities</span>
<span class="f-link" style="left:365px;top:4155px">Membership</span>
<span class="f-link" style="left:365px;top:4182px">Pictures</span>
<span class="f-link" style="left:490px;top:4075px">The Brightdesk Philosophy</span>
<span class="f-link" style="left:490px;top:4102px">Contact</span>
<span class="f-link" style="left:490px;top:4129px">Terms &amp; Conditions</span>
<span class="f-link" style="left:490px;top:4155px">Privacy Policy</span>

<div class="abs f-head" style="left:703px;top:4037px;font-size:12.5px">SUBSCRIBE OUR NEWSLETTER</div>
<div class="abs f-text" style="left:703px;top:4072px;line-height:27px">Weekly Breaking News Analysis And Cutting Edge<br>Advices On Job Searching</div>
<div class="abs f-input">Email Address</div>
<div class="btn f-sub">Subscribe</div>
<div class="abs social" style="left:702px;top:4192px"></div>
<div class="abs social" style="left:741px;top:4192px"></div>
<div class="abs social" style="left:778px;top:4192px"></div>

<div class="abs bottom-bar">
  <span style="left:111px">© 2020 brightdeskcowork | All Rights Reserved</span>
  <span style="left:888px">Home</span>
  <span style="left:941px">About</span>
  <span style="left:994px">FAQs</span>
  <span style="left:1043px">Contact</span>
</div>

</body>
</html>
```